Business cards and stationary
Maple Hollow Real Estate Investments
Simple
Teresa Vilk
Owner
4817 Lindell Ct
Larkmont, CO 80119
maplehollowrei@quillmail.example
We specialize in buying, renovating, reselling and renting homes and muti-unit properties in the Denver area
Logo
Vector logo

```html
<!DOCTYPE html>
<html lang="en">
<head>
<meta charset="utf-8">
<title>Maple Hollow Real Estate Investments – Stationery</title>
<link rel="stylesheet" href="https://fonts.googleapis.com/css2?family=PT+Serif:wght@400;700&display=swap">
<style>
  :root {
    --ink: #1c1c1c;
    --brand-red: #d7262e;
    --paper: #ffffff;
    --stage: #ffffff;
    --window-grey: #e2e2e2;
    --faint-red: #f7dcdc;
    --edge: #d9d9d9;
  }
  * { margin: 0; padding: 0; box-sizing: border-box; }
  html, body { width: 1200px; height: 881px; overflow: hidden; background: var(--stage); }
  body { position: relative; font-family: "PT Serif", Georgia, serif; color: var(--ink); }

  .piece {
    position: absolute;
    background: var(--paper);
    border: 1px solid var(--edge);
    box-shadow: 0 2px 6px rgba(0,0,0,.18);
    overflow: hidden;
  }
  .top-bar { position: absolute; left: 0; right: 0; top: 0; background: var(--ink); }
  .bottom-band { position: absolute; left: 0; right: 0; bottom: 0; background: var(--brand-red); }

  .brand { position: absolute; display: flex; align-items: center; gap: 8px; }
  .brand-square { background: var(--brand-red); flex: none; }
  .brand-name { font-weight: 700; color: var(--ink); white-space: nowrap; letter-spacing: -0.5px; }

  .faint-mark { position: absolute; background: var(--faint-red); opacity: .55; }

  /* Letterhead */
  .letterhead { left: 48px; top: 46px; width: 800px; height: 810px; }
  .letterhead .top-bar { height: 8px; }
  .letterhead .brand { left: 163px; top: 28px; }
  .letterhead .brand-square { width: 64px; height: 64px; }
  .letterhead .brand-name { font-size: 40px; }
  .letterhead .faint-mark { left: 192px; top: 398px; width: 264px; height: 216px; }
  .letterhead .footer {
    position: absolute; left: 18px; right: 18px; bottom: 18px;
    display: flex; justify-content: space-between; font-size: 12px;
  }
  .letterhead .bottom-band { height: 6px; }

  /* Envelope */
  .envelope { left: 326px; top: 175px; width: 802px; height: 334px; }
  .envelope .top-bar { height: 9px; }
  .envelope .brand { left: 34px; top: 48px; }
  .envelope .brand-square { width: 62px; height: 62px; }
  .envelope .brand-name { font-size: 40px; }
  .envelope .address-window {
    position: absolute; left: 96px; top: 172px; width: 375px; height: 81px;
    background: var(--window-grey); border: 1px solid #cfcfcf;
  }
  .envelope .faint-mark { right: 20px; top: 196px; width: 140px; height: 100px; }
  .envelope .return-address { position: absolute; right: 14px; bottom: 18px; font-size: 12px; }
  .envelope .bottom-band { height: 10px; }

  /* Business card */
  .card { left: 727px; top: 557px; width: 401px; height: 235px; }
  .card .top-bar { height: 6px; }
  .card .brand { left: 78px; top: 22px; gap: 6px; }
  .card .brand-square { width: 50px; height: 50px; }
  .card .brand-name { font-size: 30px; }
  .card .holder { position: absolute; left: 0; right: 0; top: 112px; text-align: center; }
  .card .holder-name { font-size: 18px; font-weight: 700; line-height: 1.2; }
  .card .holder-title { font-size: 13px; font-weight: 700; color: var(--brand-red); letter-spacing: 1px; line-height: 1.2; }
  .card .contact {
    position: absolute; left: 18px; top: 157px; font-size: 10px; line-height: 1.5;
  }
  .card .contact .label { display: inline-block; width: 40px; }
  .card .faint-mark { right: 10px; top: 146px; width: 84px; height: 68px; }
  .card .bottom-band { height: 7px; }
</style>
</head>
<body>

<section class="piece letterhead" aria-label="Letterhead">
  <div class="top-bar"></div>
  <div class="brand"><span class="brand-square"></span><span class="brand-name">MapleHollow</span></div>
  <div class="faint-mark"></div>
  <div class="footer">
    <span>4817 Lindell Ct Larkmont, CO 80119</span>
    <span>Email&nbsp;&nbsp; maplehollowrei@quillmail.example</span>
  </div>
  <div class="bottom-band"></div>
</section>

<section class="piece envelope" aria-label="Envelope">
  <div class="top-bar"></div>
  <div class="brand"><span class="brand-square"></span><span class="brand-name">MapleHollow</span></div>
  <div class="address-window"></div>
  <div class="faint-mark"></div>
  <div class="return-address">4817 Lindell Ct Larkmont, CO 80119</div>
  <div class="bottom-band"></div>
</section>

<section class="piece card" aria-label="Business card">
  <div class="top-bar"></div>
  <div class="brand"><span class="brand-square"></span><span class="brand-name">MapleHollow</span></div>
  <div class="holder">
    <div class="holder-name">Teresa Vilk</div>
    <div class="holder-title">OWNER</div>
  </div>
  <div class="contact">
    <div>4817 Lindell Ct</div>
    <div>Larkmont, CO 80119</div>
    <div><span class="label">Phone</span>970-555-0148</div>
    <div><span class="label">Email</span>maplehollowrei@quillmail.example</div>
  </div>
  <div class="faint-mark"></div>
  <div class="bottom-band"></div>
</section>

</body>
</html>
```